www.velmornit.com

Website design for IT outsourcing company (Velmorn IT)
Pages: Home, About Us, Services, Case Studies, Careers, Contact and more (see current website for guidance)
Include client testimonials
Include client logos (e.g., Plumtrex, etc)
List of services (staffing, app dev, integration, cloud)
Modern, clean, professional design
Blue/white/gray color scheme
Mobile and desktop responsive
Include call-to-action buttons
Space for case studies/project highlights

```html
<!DOCTYPE html>
<html lang="en">
<head>
<meta charset="utf-8">
<title>Velmorn IT — Software Development &amp; Consulting</title>
<link rel="stylesheet" href="https://fonts.googleapis.com/css2?family=Russo+One&family=Orbitron:wght@500&family=Roboto:wght@400;500;700&display=swap">
<style>
:root{
  --night:#07101f;
  --navy:#0b1a4a;
  --deep:#0d2a66;
  --royal:#1f5bd8;
  --sky:#4a90c8;
  --btn:#1d4e86;
  --steel:#8e9bb6;
  --mist:#d6d6d6;
  --white:#ffffff;
  --ink:#111111;
}
*{margin:0;padding:0;box-sizing:border-box}
html,body{width:1200px;height:4342px;overflow:hidden}
body{position:relative;background:var(--white);font-family:"Roboto",sans-serif;color:var(--ink)}
.abs{position:absolute}
.display{font-family:"Russo One",sans-serif;text-transform:uppercase;letter-spacing:1px}

/* hero */
.hero{top:0;left:0;width:1200px;height:790px}
.hero-bg{position:absolute;inset:0}
.brand-mark{left:52px;top:166px;display:flex;align-items:center;gap:10px;white-space:nowrap;color:var(--white);font-family:"Russo One",sans-serif;font-size:24px;letter-spacing:1px}
.brand-mark .dot{width:14px;height:14px;background:var(--white)}
.nav{top:44px;right:74px;display:flex;gap:48px;white-space:nowrap;font-family:"Orbitron",sans-serif;font-weight:500;font-size:14px;color:var(--white);letter-spacing:1px}
.hero-title{top:262px;left:0;width:1200px;text-align:center;color:var(--white);font-size:48px;line-height:62px}
.btn{display:flex;align-items:center;justify-content:center;border-radius:30px;color:var(--white);font-size:19px;text-transform:uppercase;background:var(--btn);white-space:nowrap}
.hero-btn{top:522px;left:503px;width:188px;height:56px;text-transform:none;font-size:20px}

.section-title{left:0;width:1200px;text-align:center;font-size:34px;white-space:nowrap}
.rule{width:52px;height:4px;background:var(--ink);left:574px}

/* why cards */
.card{width:272px;height:372px}
.card svg.frame{position:absolute;inset:0}
.card .icon{position:absolute;left:96px;top:28px;width:80px;height:80px}
.card h3{position:absolute;top:112px;left:20px;width:232px;text-align:center;font-family:"Russo One",sans-serif;font-size:15px;line-height:19px;text-transform:uppercase}
.card .bar{position:absolute;top:178px;left:110px;width:52px;height:4px;background:var(--royal)}
.card p{position:absolute;top:215px;left:28px;width:216px;text-align:center;font-size:14px;line-height:18px;color:#333}

/* value */
.value{top:1483px;left:0;width:1200px;height:561px}
.stat{width:202px;height:202px;border-radius:50%;background:var(--sky);color:var(--white);text-align:center;display:flex;flex-direction:column;align-items:center;padding-top:34px}
.stat b{font-size:56px;font-weight:500;line-height:64px}
.stat span{font-size:20px;font-weight:500;line-height:25px;color:#0e2f5c}

/* services */
.services{top:2044px;left:0;width:1200px;height:1180px}
.svc{background:var(--steel);box-shadow:0 0 0 6px #a7b2c8}
.svc .photo{position:absolute;left:10px;top:10px;right:10px;height:357px}
.svc h3{position:absolute;left:0;right:0;top:420px;text-align:center;color:var(--deep);font-size:28px;line-height:36px;font-family:"Russo One",sans-serif;text-transform:uppercase}
.svc p{position:absolute;left:44px;right:48px;font-size:16.5px;line-height:22px;color:#111}
.svc .btn{position:absolute;left:44px;width:208px;height:56px;background:var(--deep)}

/* brands */
.brands-row{top:3440px;left:0;width:1200px;height:60px}
.brand{position:absolute;top:0;height:60px;display:flex;align-items:center;gap:8px;white-space:nowrap;font-family:"Roboto",sans-serif;font-weight:500;color:#3a3f48}
.brand .sq{width:22px;height:22px;border-radius:50%;background:#3a3f48}

/* consult */
.consult{top:3547px;left:0;width:1200px;height:516px}
.consult h2{position:absolute;left:119px;top:202px;color:var(--white);font-size:38px;line-height:50px;white-space:nowrap}
.consult p{position:absolute;left:119px;top:316px;width:480px;color:var(--white);font-size:20px;line-height:27px}
.field{position:absolute;left:679px;width:402px;height:57px;border-radius:30px;background:rgba(255,255,255,.85);color:#333;font-size:14px;letter-spacing:1.5px;padding-left:26px;display:flex;align-items:center}
.submit{left:679px;top:413px;width:182px;height:56px;background:var(--deep);font-size:20px}

/* footer */
.footer{top:4061px;left:0;width:1200px;height:281px;background:var(--night);color:var(--white)}
.foot-links{position:absolute;top:66px;font-size:11px;letter-spacing:1.3px;line-height:24px;text-transform:uppercase;white-space:nowrap}
.contact{position:absolute;top:200px;display:flex;align-items:center;gap:14px;font-size:9.5px;line-height:12px;white-space:nowrap}
.contact .ic{width:30px;height:30px;border-radius:50%;background:#2f7bd6;display:flex;align-items:center;justify-content:center}
.foot-brand{position:absolute;left:893px;top:212px;display:flex;align-items:center;gap:12px;white-space:nowrap;font-family:"Russo One",sans-serif;font-size:32px;letter-spacing:1px}
.foot-brand .dot{width:18px;height:18px;background:var(--white)}
</style>
</head>
<body>

<header class="abs hero">
  <svg class="hero-bg" width="1200" height="790" viewBox="0 0 1200 790">
    <defs>
      <radialGradient id="heroGlow" cx="0.55" cy="0.35" r="0.8">
        <stop offset="0" stop-color="#173a55"/>
        <stop offset="0.6" stop-color="#0a1a2a"/>
        <stop offset="1" stop-color="#050a12"/>
      </radialGradient>
    </defs>
    <polygon points="0,0 1200,0 1200,600 600,745 0,600" fill="url(#heroGlow)" role="img" aria-label="Dark blue network of connected lines and nodes"/>
    <polygon points="25,615 600,775 1180,615 600,748" fill="var(--navy)"/>
  </svg>
  <div class="abs brand-mark"><span class="dot"></span>VELMORN IT</div>
  <nav class="abs nav"><span>Home</span><span>Solutions</span><span>Consulting</span><span>Who We Serve</span><span>Insights</span><span>Contact</span></nav>
  <h1 class="abs hero-title display">Speed up the process of<br>developing your<br>software with confidence</h1>
  <a class="abs btn hero-btn">GET IN TOUCH</a>
</header>

<h2 class="abs section-title display" style="top:862px">Why businesses choose Velmorn</h2>
<div class="abs rule" style="top:912px"></div>

<div class="abs card" style="left:137px;top:1028px">
  <svg class="frame" width="272" height="372" viewBox="0 0 272 372"><path d="M2,2 H270 V310 L136,370 L2,310 Z" fill="#fff" stroke="var(--royal)" stroke-width="2"/><path d="M-6,306 L136,366 L278,306 L278,314 L136,374 L-6,314Z" fill="var(--royal)"/></svg>
  <svg class="icon" viewBox="0 0 80 80"><g fill="none" stroke="var(--royal)" stroke-width="3"><rect x="8" y="48" width="10" height="20"/><rect x="24" y="38" width="10" height="30"/><rect x="40" y="28" width="10" height="40"/><path d="M44 6h18v8a9 9 0 0 1-18 0z"/><path d="M53 23v6"/><circle cx="62" cy="58" r="11"/><path d="M56 58l4 4 8-8"/></g></svg>
  <h3>Proven software<br>success</h3><div class="bar"></div>
  <p>Our ability to develop our own software in-house and serve more than 20 clients distinguishes us from other companies..</p>
</div>

<div class="abs card" style="left:464px;top:1018px;filter:drop-shadow(0 0 8px rgba(0,0,0,.25))">
  <svg class="frame" width="272" height="372" viewBox="0 0 272 372"><path d="M2,2 H270 V310 L136,370 L2,310 Z" fill="#fff" stroke="var(--royal)" stroke-width="2"/><path d="M-6,306 L136,366 L278,306 L278,314 L136,374 L-6,314Z" fill="var(--royal)"/></svg>
  <svg class="icon" viewBox="0 0 80 80"><g fill="none" stroke="var(--royal)" stroke-width="3"><circle cx="40" cy="22" r="12"/><path d="M36 34v6h8v-6"/><path d="M40 2v4M22 8l3 3M58 8l-3 3"/><path d="M6 56h14l20 8 24-12"/><rect x="2" y="50" width="8" height="22" fill="var(--royal)"/></g></svg>
  <h3>Deliver<br>innovative<br>solutions</h3><div class="bar" style="top:196px"></div>
  <p style="top:222px">We bring your software visions to life by leveraging emerging technologies.</p>
</div>

<div class="abs card" style="left:793px;top:1028px">
  <svg class="frame" width="272" height="372" viewBox="0 0 272 372"><path d="M2,2 H270 V310 L136,370 L2,310 Z" fill="#fff" stroke="var(--royal)" stroke-width="2"/><path d="M-6,306 L136,366 L278,306 L278,314 L136,374 L-6,314Z" fill="var(--royal)"/></svg>
  <svg class="icon" viewBox="0 0 80 80"><g fill="none" stroke="var(--royal)" stroke-width="3"><circle cx="48" cy="44" r="22"/><path d="M48 44V30M42 12h12M48 12v10M66 24l4-4"/><path d="M4 36h14M8 46h12M4 56h14"/></g></svg>
  <h3>Fastrack to<br>market</h3><div class="bar"></div>
  <p>Attain quicker time-to-market to surpass competitors by implementing continuous delivery cycles.</p>
</div>

<section class="abs value">
  <svg class="abs" style="inset:0" width="1200" height="561" role="img" aria-label="Blue digital technology backdrop with glowing circuitry">
    <defs><linearGradient id="valueBg" x1="0" y1="0" x2="0" y2="1"><stop offset="0" stop-color="#0a1e5a"/><stop offset="0.55" stop-color="#123a7c"/><stop offset="1" stop-color="#1b2a6a"/></linearGradient></defs>
    <rect width="1200" height="561" fill="url(#valueBg)"/>
  </svg>
  <h2 class="abs section-title display" style="top:89px;color:var(--white)">We bring value</h2>
  <div class="abs rule" style="top:140px;background:var(--white)"></div>
  <div class="abs stat" style="left:44px;top:258px"><b>100+</b><span>Trained<br>Professionals</span></div>
  <div class="abs stat" style="left:270px;top:258px"><b>25+</b><span>Years Of<br>Industry<br>Experience</span></div>
  <div class="abs stat" style="left:497px;top:258px"><b>24/7</b><span>Availability</span></div>
  <div class="abs stat" style="left:725px;top:258px"><b>$100</b><span>Starts at Low<br>Costs</span></div>
  <div class="abs stat" style="left:954px;top:258px"><b>60%</b><span>Approximated<br>Cost Savings</span></div>
</section>

<section class="abs services">
  <svg class="abs" style="left:0;top:0" width="1200" height="1180" viewBox="0 0 1200 1180">
    <polygon points="0,0 1200,0 1200,1040 600,1130 0,1040" fill="var(--mist)"/>
    <polygon points="0,1040 600,1130 1200,1040 1200,1052 600,1176 0,1052" fill="var(--navy)"/>
    <polygon points="617,950 656,1010 617,1070 578,1010" fill="#e9e9e9"/>
  </svg>
  <h2 class="abs section-title display" style="top:98px">Services we offer</h2>
  <div class="abs rule" style="top:150px"></div>

  <article class="abs svc" style="left:61px;top:214px;width:520px;height:766px">
    <div class="photo" role="img" aria-label="Human hand reaching toward a robotic hand over a glowing digital interface" style="background:linear-gradient(135deg,#0c2b52,#1f5f8f 55%,#0b2240)"></div>
    <h3>Software development<br>services</h3>
    <p style="top:514px">Accelerate the time it takes to launch your product and shorten the feedback loop with developers, starting with building the minimum viable product (MVP) up to incorporating artificial intelligence (AI) features. Foster creativity by implementing a testing approach that empowers you to release dependable code with certainty.</p>
    <a class="btn" style="top:674px">LEARN MORE</a>
  </article>

  <article class="abs svc" style="left:646px;top:211px;width:493px;height:769px">
    <div class="photo" role="img" aria-label="Two colleagues reviewing work together at a laptop" style="background:linear-gradient(135deg,#cfc6bb,#8a8f99 55%,#e2e2e2)"></div>
    <h3 style="top:436px">Consulting services</h3>
    <p style="top:521px">Utilize the knowledge and experience at Velmorn IT in software development to facilitate informed decision-making for your organization's technological systems. Enhance the efficiency of your team and the value of your product with expert advise from experienced individuals.</p>
    <a class="btn" style="top:680px">LEARN MORE</a>
  </article>
</section>

<h2 class="abs section-title display" style="top:3301px">Brands that trust us</h2>
<div class="abs rule" style="top:3352px"></div>
<div class="abs brands-row">
  <svg class="abs" style="left:62px;top:6px" width="26" height="48"><path d="M22 2 L4 24 L22 46" fill="none" stroke="#c9c9c9" stroke-width="6"/></svg>
  <div class="brand" style="left:132px;font-size:32px">Brixwell</div>
  <div class="brand" style="left:317px;font-size:38px"><span class="sq"></span>Tandemly</div>
  <div class="brand" style="left:614px;font-size:18px">Summit Loom</div>
  <div class="brand" style="left:836px;font-size:18px"><span class="sq" style="border-radius:0"></span>Orvane</div>
  <div class="brand" style="left:941px;font-size:20px">Quaymark</div>
  <svg class="abs" style="left:1118px;top:6px" width="26" height="48"><path d="M4 2 L22 24 L4 46" fill="none" stroke="#c9c9c9" stroke-width="6"/></svg>
</div>

<section class="abs consult">
  <svg class="abs" style="inset:0" width="1200" height="516" viewBox="0 0 1200 516">
    <defs><linearGradient id="consultBg" x1="0" y1="0" x2="1" y2="1"><stop offset="0" stop-color="#0b2c8a"/><stop offset="0.5" stop-color="#1645a8"/><stop offset="1" stop-color="#0a1d5c"/></linearGradient></defs>
    <rect width="1200" height="516" fill="url(#consultBg)" role="img" aria-label="Blue binary code and circuitry backdrop"/>
    <polygon points="0,0 1200,0 600,94" fill="var(--white)"/>
  </svg>
  <h2 class="display">Schedule a free<br>consultation today.</h2>
  <p>Please inform us of your business requirements, and we would be delighted to demonstrate how we can assist you.</p>
  <div class="field" style="top:135px">NAME:</div>
  <div class="field" style="top:204px">COMPANY:</div>
  <div class="field" style="top:270px">COMPANY EMAIL ADDRESS :</div>
  <div class="field" style="top:337px">WHAT CAN WE DO TO ASSIST YOU?</div>
  <a class="abs btn submit">SUBMIT</a>
</section>

<footer class="abs footer">
  <div class="foot-links" style="left:115px">Home<br>Solutions<br>Consulting<br>Who We Serve</div>
  <div class="foot-links" style="left:285px;top:64px">Blogs<br>About Us<br>Offshore Development<br>Why Nepal?</div>
  <div class="contact" style="left:105px">
    <span class="ic"><svg width="14" height="18" viewBox="0 0 14 18"><path d="M7 1a6 6 0 0 0-6 6c0 4 6 10 6 10s6-6 6-10a6 6 0 0 0-6-6z" fill="#fff"/><circle cx="7" cy="7" r="2.2" fill="#2f7bd6"/></svg></span>
    <span>VELMORN IT, Orchid House<br>Kestrel Road 2033</span>
  </div>
  <div class="contact" style="left:336px">
    <span class="ic"><svg width="16" height="16" viewBox="0 0 16 16"><path d="M3 1l3 3-2 2c1 2 3 4 5 5l2-2 3 3-2 3C6 15 1 10 1 3z" fill="#fff"/></svg></span>
    <span>Office Number:<br>+1 (555) 014-2290</span>
  </div>
  <div class="contact" style="left:555px">
    <span class="ic"><svg width="16" height="12" viewBox="0 0 16 12"><rect x="1" y="1" width="14" height="10" fill="#fff"/><path d="M1 1l7 6 7-6" fill="none" stroke="#2f7bd6" stroke-width="1.4"/></svg></span>
    <span>Email:<br>info@velmornit.com</span>
  </div>
  <div class="foot-brand"><span class="dot"></span>VELMORN IT</div>
</footer>

</body>
</html>
```